QuarryNest - Webstartup looking for some style

QuarryNest is a cloud based web application that allows construction sub-contractors to create and manage bids. Generally, these contractors will contact subcontractors to have them do specific parts of a larger construction project. This would be used by various subcontractors including woodwork (cabinetry), electricians, masons, etc...

Nearly all competitors are clients applications that have to be installed on the computer and are very expensive. This is a much lower cost alternative.

The business is just beginning and we want people to view us as a fresh alternative to companies that have been around for a long time and are starting to look a little dated.

We would like our logo included on the card (see attached). We have been using the circular 'qn' emblem seperately from the complete logo in various areas of the website. We lean towards a professional and clean look, with a tendancy more towards modern.

We want to differentiate ourselves from our competition which tend to be dated, complicated and less graphical.

(We are currently designing our public website as well - but don't have any designs yet)

Industry/Entity Type

Construction

Requirements
Must have
• Circular 'qn' emblem from logo. Probably entire logo, but not necessarily.

Should have reference to website: www.quarrynest-demo.net

The Url should be all lowercase (www.quarrynest-demo.net)
Should not have
• we do not want to list a phone number or email address on the cards. we want people to go to the actual website. we haven't decided if we want names printed on the business cards.

```html
<!DOCTYPE html>
<html lang="en">
<head>
<meta charset="utf-8">
<title>QuarryNest Business Card</title>
<link href="https://fonts.googleapis.com/css2?family=Arimo:wght@400;700&display=swap" rel="stylesheet">
<style>
  :root {
    --page-bg: #e6e7e9;
    --blue-deep: #1f86cf;
    --blue-mid: #2b9de0;
    --blue-light: #4cc0f0;
    --orange: #f7941d;
    --navy-text: #23507a;
    --card-white: #f6f6f6;
    --grey-text: #555a5f;
    --divider: #b9bcc0;
  }
  * { box-sizing: border-box; margin: 0; padding: 0; }
  html, body {
    width: 1200px; height: 1000px; overflow: hidden;
    background: var(--page-bg);
    font-family: "Arimo", Arial, sans-serif;
  }
  .canvas { position: relative; width: 1200px; height: 1000px; }

  .card {
    position: absolute; width: 660px; height: 360px;
    border-radius: 26px; overflow: hidden;
    box-shadow: 0 6px 18px rgba(0,0,0,0.18);
  }

  /* Front */
  .card-front {
    left: 90px; top: 90px;
    background: radial-gradient(ellipse 70% 80% at 50% 85%, var(--blue-light) 0%, var(--blue-mid) 55%, var(--blue-deep) 100%);
  }
  .card-front .gloss { position: absolute; inset: 0; }
  .front-mark {
    position: absolute; left: 0; right: 0; top: 140px;
    display: flex; align-items: center; justify-content: center; gap: 12px;
  }
  .emblem-dot { width: 46px; height: 46px; border-radius: 50%; background: var(--orange); flex: none; }
  .front-mark .brand-name { color: #ffffff; font-size: 30px; font-weight: 700; }
  .front-rule {
    position: absolute; left: 190px; right: 190px; top: 312px;
    height: 1px; background: rgba(20,60,100,0.35);
  }
  .front-url {
    position: absolute; left: 0; right: 0; top: 322px;
    text-align: center; color: var(--navy-text);
    font-size: 16px; font-weight: 700; letter-spacing: 3px;
  }

  /* Back */
  .card-back { left: 450px; top: 540px; background: var(--card-white); }
  .card-back .sweep { position: absolute; inset: 0; }
  .back-mark {
    position: absolute; left: 78px; top: 236px;
    display: flex; align-items: center; gap: 10px;
  }
  .back-mark .emblem-dot { width: 36px; height: 36px; background: var(--blue-mid); }
  .back-mark .brand-name { color: var(--blue-deep); font-size: 20px; font-weight: 700; }
  .dotted-divider {
    position: absolute; left: 300px; top: 110px; height: 200px;
    border-left: 2px dotted var(--divider);
  }
  .contact {
    position: absolute; right: 40px; top: 186px; text-align: right; color: var(--grey-text);
  }
  .contact .rule { height: 1px; background: var(--divider); margin: 0 0 10px 40px; }
  .contact .url { font-size: 22px; font-weight: 700; }
</style>
</head>
<body>
<main class="canvas">

  <section class="card card-front" aria-label="Card front">
    <svg class="gloss" viewBox="0 0 660 360" width="660" height="360" aria-hidden="true">
      <path d="M0,0 H660 V70 C480,60 200,110 0,260 Z" fill="#ffffff" opacity="0.08"/>
    </svg>
    <div class="front-mark">
      <span class="emblem-dot"></span>
      <span class="brand-name">QuarryNest</span>
    </div>
    <div class="front-rule"></div>
    <p class="front-url">www.quarrynest-demo.net</p>
  </section>

  <section class="card card-back" aria-label="Card back">
    <svg class="sweep" viewBox="0 0 660 360" width="660" height="360" aria-hidden="true">
      <path d="M0,0 H660 V16 H340 C230,40 70,170 0,340 V360 H0 Z" fill="var(--orange)"/>
      <path d="M0,0 H660 V14 H330 C220,38 60,165 0,330 Z" fill="var(--blue-deep)"/>
    </svg>
    <div class="back-mark">
      <span class="emblem-dot"></span>
      <span class="brand-name">QuarryNest</span>
    </div>
    <div class="dotted-divider"></div>
    <div class="contact">
      <div class="rule"></div>
      <p class="url">www.quarrynest-demo.net</p>
    </div>
  </section>

</main>
</body>
</html>
```